Business Card Design

We currently have a business card design for our main business 'Lantern Walls"
We are reasonably happy with our current design for Lantern Walls business card (black damask patterned wallpaper in background white simplistic font with white chandelier (see logo on website). www.lanternwalls.com.au

We are considering whether its in our best interest to have a separate business card OR a double sided card to promote our secondary business 'Glow Cones'. We are open to either a double-sided card with one business on each side OR a double sided card for each business. With contact info on the back of each.

We need a new snazzy design for 'Glow Cones' our custom made lampshades from which we craft from our wallpaper designs. We had an idea that we could use the top swatch shown on this link below as the pattern in the background (Orange/black) geometric triangles.
http://www.lanternwalls.com.au/product_info.php?products_id=1086

For the glow cones Font we would be happy with something similar to Lantern Walls but perhaps a little more handmade/arty slant.
Below another link shows you a few of our lampshades
http://www.lanternwalls.com.au/index.php?cPath=10

For Glow Cones I think we also need the quote under in smaller font
"Custom-Made Wallpaper Lampshades"

Target Market(s)

Glow Cones will be for the Young Funky Apartment Dwellers, Young Families Styling Home Decor and Kids Rooms. It also attracts small business owners doing shop-fits.

Industry/Entity Type

Business

Contact Information for Business Card

We need to incorporate our sister business to the back side of our business card. I am also open to having two different business cards if designers think this will not be possible.
We need the same contact info, different logo.
ABN: 47 302 916 584
Email: sales@lanternwalls.com.au
Postal Address: PO Box 731, Kelvale VIC 3294
Website: http://www.lanternwalls.com.au

Requirements
Must have
• A hand-made arty appeal for Glow Cones
Was unable to get sliders to work for the look and feel so below is the best list from the above:
Bold, Playful, Modern, Personable, Colorful, Upmarket.
Nice to have
• We love the bold contrasting colors. Colors chosen for our website were Orange, Blue and Duck Egg Bright Blue!

```html
<!DOCTYPE html>
<html lang="en">
<head>
<meta charset="utf-8">
<title>Glow Cones – Business Card</title>
<link rel="stylesheet" href="https://fonts.googleapis.com/css2?family=Varela+Round&family=Source+Sans+3:wght@400&display=swap">
<style>
  :root {
    --page: #ffffff;
    --ink-panel: #2c2733;
    --white: #ffffff;
    --pill-ink: #2c2733;
    --tri-pink: #ef9aa0;
    --tri-rose: #e2566f;
    --tri-grey: #a9a9ab;
    --tri-slate: #474b54;
    --tri-lime: #d8dd4f;
    --tri-orange: #ed943c;
  }
  html, body {
    margin: 0;
    width: 1200px;
    height: 900px;
    overflow: hidden;
    background: var(--page);
  }
  .canvas {
    position: relative;
    width: 1200px;
    height: 900px;
  }
  .card {
    position: absolute;
    left: 82px;
    top: 149px;
    width: 1061px;
    height: 600px;
    overflow: hidden;
  }
  .card-art {
    position: absolute;
    inset: 0;
    width: 100%;
    height: 100%;
  }
  .brand-pill {
    position: absolute;
    left: 361px;
    top: 93px;
    width: 479px;
    height: 100px;
    box-sizing: border-box;
    border: 4px solid var(--pill-ink);
    border-radius: 50px;
    background: var(--white);
    display: flex;
    align-items: center;
    justify-content: center;
  }
  .brand-name {
    margin: 0;
    font-family: "Varela Round", sans-serif;
    font-weight: 400;
    font-size: 62px;
    color: var(--pill-ink);
    letter-spacing: 0.5px;
    line-height: 1;
    padding-bottom: 4px;
  }
  .tagline {
    position: absolute;
    left: 864px;
    top: 104px;
    margin: 0;
    font-family: "Varela Round", sans-serif;
    font-size: 22px;
    line-height: 28px;
    color: var(--white);
  }
  .contact {
    position: absolute;
    left: 588px;
    top: 406px;
    margin: 0;
    padding: 0;
    list-style: none;
    font-family: "Source Sans 3", sans-serif;
    font-size: 22px;
    line-height: 40.5px;
    color: var(--white);
  }
  .contact li:first-child { padding-left: 6px; }
</style>
</head>
<body>
<div class="canvas">
  <section class="card">
    <svg class="card-art" viewBox="0 0 1061 600" preserveAspectRatio="none">
      <defs>
        <linearGradient id="triangle-tones" x1="0" y1="0" x2="1" y2="1">
          <stop offset="0" stop-color="var(--tri-pink)"/>
          <stop offset="0.3" stop-color="var(--tri-grey)"/>
          <stop offset="0.55" stop-color="var(--tri-lime)"/>
          <stop offset="0.8" stop-color="var(--tri-rose)"/>
          <stop offset="1" stop-color="var(--tri-orange)"/>
        </linearGradient>
      </defs>
      <rect class="pattern-field" width="1061" height="600" fill="url(#triangle-tones)" role="img" aria-label="Colourful geometric triangle wallpaper pattern in pink, grey, lime, orange and slate"/>
      <path class="contact-panel" d="M728,0 C790,40 800,150 760,230 C720,300 640,340 600,420 C570,480 552,540 548,600 L1061,600 L1061,0 Z" fill="var(--ink-panel)"/>
    </svg>
    <div class="brand-pill"><h1 class="brand-name">Glow Cones</h1></div>
    <p class="tagline">Custom-Made<br>Wallpaper<br>Lampshades</p>
    <ul class="contact">
      <li>ABN : 47 302 916 584</li>
      <li>Email : sales@lanternwalls.com.au</li>
      <li>Add &nbsp;: PO Box 731, Kelvale VIC 3294</li>
      <li>Web : http://www.lanternwalls.com.au</li>
    </ul>
  </section>
</div>
</body>
</html>
```